Allies for Wellness Resources- Medical Billing and Consultant Firm Business card

We need a logo design for a medical billing and healthcare consulting firm. We help physician medical practices achieve their financial objectives by providing medical billing services and other revenue cycle services. We want a business card design that is eye catching and compliments the color and design my logo. We like variations of blue colors however we are very open to other colors. We would like the services we provide listed on the back of the card.

Target Market(s)

Doctors and medical practices

Industry/Entity Type

Medical

Contact Information for Business Card

Space for logo, name, title, phone #, address, web address

Font styles to use
Serif
Sans Serif

Colors

Designer to choose colors to be used in the design.

Requirements
Must have
• Company Services listed on the back.
Should not have
• We are pretty open to all design ideas

```html
<!DOCTYPE html>
<html lang="en">
<head>
<meta charset="utf-8">
<title>Allies for Wellness Resources – Business Card</title>
<link rel="stylesheet" href="https://fonts.googleapis.com/css2?family=Cinzel:wght@400;700&family=Questrial&display=swap">
<style>
  :root {
    --page-bg: #e9e6e1;
    --white: #ffffff;
    --paper: #f3f4f5;
    --paper-shade: #dfe1e3;
    --blue-deep: #0f5fb4;
    --blue-mid: #1a7fd0;
    --blue-light: #2a93dd;
    --cyan-band: #3cb0d6;
    --cyan-band-dark: #2c9cc6;
    --ink-blue: #1a6fc0;
    --ink-dark: #3b3f44;
    --serif: "Cinzel", "Times New Roman", serif;
    --sans: "Questrial", "Helvetica Neue", Arial, sans-serif;
  }
  * { box-sizing: border-box; margin: 0; padding: 0; }
  html, body { width: 1200px; height: 780px; overflow: hidden; }
  body {
    background: var(--page-bg);
    display: flex;
    align-items: center;
    justify-content: center;
    gap: 100px;
  }
  .card {
    position: relative;
    width: 360px;
    height: 630px;
    border-radius: 22px;
    overflow: hidden;
    box-shadow: 0 10px 28px rgba(0,0,0,0.18);
  }
  .brand-dot {
    display: block;
    width: 30px;
    height: 30px;
    border-radius: 50%;
    background: var(--ink-blue);
  }

  /* ---------- Front ---------- */
  .card-front {
    background: linear-gradient(180deg, var(--white) 0%, var(--paper) 45%, var(--paper-shade) 100%);
  }
  .front-waves {
    position: absolute;
    inset: 0;
    width: 100%;
    height: 100%;
  }
  .brand {
    position: absolute;
    top: 90px;
    left: 0;
    right: 0;
    text-align: center;
    display: flex;
    flex-direction: column;
    align-items: center;
    gap: 14px;
  }
  .brand-name {
    font-family: var(--serif);
    font-weight: 400;
    font-size: 17px;
    letter-spacing: 0.5px;
    color: var(--ink-dark);
  }
  .contact {
    position: absolute;
    top: 300px;
    left: 0;
    right: 0;
    text-align: center;
    color: var(--white);
  }
  .person-name {
    font-family: var(--serif);
    font-weight: 700;
    font-size: 21px;
    letter-spacing: 1px;
    line-height: 1.2;
  }
  .person-title {
    font-family: var(--sans);
    font-size: 16px;
    line-height: 1.3;
  }
  .divider {
    width: 250px;
    height: 1px;
    margin: 8px auto 6px;
    background: linear-gradient(90deg, transparent, rgba(255,255,255,0.75), transparent);
  }
  .contact-icon {
    display: block;
    margin: 0 auto 3px;
    width: 19px;
    height: 19px;
  }
  .contact-line {
    font-family: var(--sans);
    font-size: 16px;
    line-height: 1.3;
  }
  .footer-band {
    position: absolute;
    left: 0;
    right: 0;
    bottom: 0;
    height: 66px;
    background: linear-gradient(180deg, var(--cyan-band), var(--cyan-band-dark));
    border-top: 4px solid var(--white);
    display: flex;
    align-items: center;
    justify-content: center;
  }
  .website {
    font-family: var(--sans);
    font-size: 17px;
    color: var(--white);
    letter-spacing: 0.3px;
  }

  /* ---------- Back ---------- */
  .card-back {
    background: radial-gradient(ellipse at 50% 45%, var(--blue-light) 0%, var(--blue-mid) 45%, var(--blue-deep) 100%);
  }
  .back-content {
    position: absolute;
    top: 200px;
    left: 0;
    right: 0;
    text-align: center;
    color: var(--white);
  }
  .back-content .brand-dot {
    margin: 0 auto 14px;
    background: var(--white);
  }
  .back-brand {
    font-family: var(--serif);
    font-weight: 400;
    font-size: 17px;
    letter-spacing: 0.5px;
    margin-bottom: 18px;
  }
  .services {
    list-style: none;
    font-family: var(--sans);
    font-size: 16px;
    line-height: 1.35;
  }
  .back-content .website {
    display: block;
    margin-top: 20px;
  }
</style>
</head>
<body>

  <section class="card card-front" aria-label="Business card front">
    <svg class="front-waves" viewBox="0 0 360 630" preserveAspectRatio="none" aria-hidden="true">
      <defs>
        <linearGradient id="frontBlue" x1="0" y1="0" x2="0" y2="1">
          <stop offset="0" stop-color="#1a86d6"/>
          <stop offset="1" stop-color="#0f5fb4"/>
        </linearGradient>
        <linearGradient id="cyanWave" x1="0" y1="0" x2="1" y2="0">
          <stop offset="0" stop-color="#3cb0d6"/>
          <stop offset="1" stop-color="#1a7fd0"/>
        </linearGradient>
      </defs>
      <path d="M0 246 C 110 222, 250 232, 360 296 L 360 630 L 0 630 Z" fill="url(#cyanWave)"/>
      <path d="M0 258 C 115 236, 250 246, 360 310 L 360 630 L 0 630 Z" fill="url(#frontBlue)"/>
      <path d="M60 264 C 170 254, 280 274, 360 322" fill="none" stroke="#ffffff" stroke-width="3" stroke-linecap="round"/>
    </svg>

    <header class="brand">
      <span class="brand-dot" aria-hidden="true"></span>
      <h1 class="brand-name">Allies for Wellness Resources LLC</h1>
    </header>

    <div class="contact">
      <h2 class="person-name">DANIEL MOORE</h2>
      <p class="person-title">Founder</p>
      <div class="divider"></div>
      <svg class="contact-icon" viewBox="0 0 22 22" aria-hidden="true">
        <circle cx="11" cy="11" r="10" fill="#ffffff"/>
        <path d="M6 9 Q11 5 16 9 L14.5 10.5 L13 9.5 L9 9.5 L7.5 10.5 Z M7.5 11.5 H14.5 L15.5 16 H6.5 Z" fill="#1a7fd0"/>
      </svg>
      <p class="contact-line phone">(555) 014-2290</p>
      <div class="divider"></div>
      <svg class="contact-icon" viewBox="0 0 22 22" aria-hidden="true">
        <circle cx="11" cy="11" r="10" fill="#ffffff"/>
        <rect x="5.5" y="7" width="11" height="8" fill="none" stroke="#1a7fd0" stroke-width="1.4"/>
        <path d="M5.5 7 L11 11.5 L16.5 7" fill="none" stroke="#1a7fd0" stroke-width="1.4"/>
      </svg>
      <p class="contact-line email">hello@allieswellness.com</p>
      <div class="divider"></div>
      <p class="contact-line address">PO BOX 480 Harbor Lane<br>4th street Geelong</p>
    </div>

    <footer class="footer-band">
      <span class="website">www.allieswellness.com</span>
    </footer>
  </section>

  <section class="card card-back" aria-label="Business card back">
    <div class="back-content">
      <span class="brand-dot" aria-hidden="true"></span>
      <h2 class="back-brand">Allies for Wellness Resources LLC</h2>
      <ul class="services">
        <li>Local Community Marketing</li>
        <li>Word-of-Mouth Marketing</li>
        <li>B2B Marketing</li>
        <li>Special Projects and Event Marketing</li>
      </ul>
      <span class="website">www.allieswellness.com</span>
    </div>
    <footer class="footer-band"></footer>
  </section>

</body>
</html>
```